Upmarket building and construction company needs signage

Our building company R Brent Construction, needs signage to put up on the side of our vehicle trailers and on site fencing. We are a building company that specialises in residential construction and carpentry .

I will attach our logo and some inspirational pics for site fencing as well as what our trailer looks like .
Other details i would like on the sign are our
( email) rbrentconstruction@mailbox-example.net
(mobile ) 0493 518 264
(website ) rbrentconstruction. example.net

Target Market(s)

Home owners looking for a reliable local builder who produces good quality work. I have attached some inspirational pics.

Industry/Entity Type

Building and Construction

Colors

Designer to choose colors to be used in the design.

Requirements
Must have
• Our logo, contact information
Nice to have
• We would like the design to have elements of being Elegant, Serious, Modern, Professional, Masculine, Conservative and Upmarket.

```html
<!DOCTYPE html>
<html lang="en">
<head>
<meta charset="utf-8">
<title>R Brent Construction – Signage</title>
<link rel="stylesheet" href="https://fonts.googleapis.com/css2?family=Jost:wght@300;400&display=swap">
<style>
:root{
  --bg:#cdced0;
  --panel:#231f20;
  --mark:#858585;
  --ink:#ececec;
  --ink-soft:#8e8e8e;
  --rule:#6e6e6e;
  --steel-a:#b9bcc1;
  --steel-b:#e3e5e8;
}
*{margin:0;padding:0;box-sizing:border-box}
html,body{width:1200px;height:1200px;overflow:hidden;background:var(--bg)}
body{position:relative;font-family:'Jost',sans-serif;font-weight:300;color:var(--ink)}
.sign{position:absolute;background:var(--panel);overflow:hidden}
.sign--wide{top:59px;width:528px;height:263px}
.sign--card{top:977px;width:327px;height:163px}
.wordmark{position:absolute;color:var(--mark);font-weight:300;text-transform:uppercase;line-height:1.15;letter-spacing:.12em;white-space:nowrap}
.wordmark span{display:block}
.tagline{position:absolute;line-height:1.3;white-space:nowrap}
.contacts{position:absolute;list-style:none}
.contacts li{display:flex;align-items:center;white-space:nowrap}
.contacts svg{flex:none;stroke:var(--ink);fill:none;stroke-width:1.4}
.rule{position:absolute;height:1px;background:var(--rule)}
.trailer-photo{position:absolute;left:40px;top:354px;width:1093px;height:590px;border-radius:4px;
  background:linear-gradient(160deg,var(--steel-b),var(--steel-a) 55%,#9fa3a8)}
</style>
</head>
<body>

<svg width="0" height="0" style="position:absolute">
  <symbol id="i-phone" viewBox="0 0 12 12"><rect x="3" y="1" width="6" height="10" rx="1"/><line x1="5" y1="9" x2="7" y2="9"/></symbol>
  <symbol id="i-mail" viewBox="0 0 12 12"><rect x="1" y="3" width="10" height="7"/><polyline points="1,3 6,7 11,3"/></symbol>
  <symbol id="i-web" viewBox="0 0 12 12"><circle cx="6" cy="6" r="4.6"/><ellipse cx="6" cy="6" rx="2" ry="4.6"/><line x1="1.4" y1="6" x2="10.6" y2="6"/></symbol>
</svg>

<!-- Sign A: centred -->
<section class="sign sign--wide" style="left:60px">
  <div class="wordmark" style="left:0;right:0;top:78px;text-align:center;font-size:14px"><span>R Brent</span><span>Construction</span></div>
  <div class="rule" style="left:180px;width:200px;top:158px"></div>
  <ul class="contacts" style="left:180px;top:170px;font-size:11px">
    <li style="height:15.5px"><svg width="9" height="9" style="margin-right:9px"><use href="#i-phone"/></svg>0493 518 264</li>
    <li style="height:15.5px"><svg width="9" height="9" style="margin-right:9px"><use href="#i-mail"/></svg>rbrentconstruction@mailbox-example.net</li>
    <li style="height:15.5px"><svg width="9" height="9" style="margin-right:9px"><use href="#i-web"/></svg>rbrentconstruction. example.net</li>
  </ul>
  <div class="rule" style="left:180px;width:200px;top:226px"></div>
</section>

<!-- Sign B: left mark, right contacts -->
<section class="sign sign--wide" style="left:607px">
  <div class="wordmark" style="left:27px;top:70px;font-size:20px"><span>R Brent</span><span>Construction</span></div>
  <p class="tagline" style="left:29px;top:222px;font-size:10.5px">Residential Construction<br>and Carpentry</p>
  <ul class="contacts" style="right:24px;top:199px;font-size:11px">
    <li style="height:15.5px"><svg width="9" height="9" style="margin-right:9px"><use href="#i-phone"/></svg>0493 518 264</li>
    <li style="height:15.5px"><svg width="9" height="9" style="margin-right:9px"><use href="#i-mail"/></svg>rbrentconstruction@mailbox-example.net</li>
    <li style="height:15.5px"><svg width="9" height="9" style="margin-right:9px"><use href="#i-web"/></svg>rbrentconstruction. example.net</li>
  </ul>
</section>

<div class="trailer-photo" role="img" aria-label="Galvanised tandem box trailer with the dark sign panels mounted on its cage sides"></div>

<!-- Card 1 -->
<section class="sign sign--card" style="left:71px">
  <p class="tagline" style="left:19px;top:9px;font-size:9.5px">Residential Construction<br>and Carpentry</p>
  <div class="wordmark" style="left:0;right:0;top:66px;text-align:center;font-size:11px"><span>R Brent</span><span>Construction</span></div>
  <ul class="contacts" style="right:14px;top:121px;font-size:6.5px">
    <li style="height:9.5px"><svg width="6" height="6" style="margin-right:5px"><use href="#i-phone"/></svg>0493 518 264</li>
    <li style="height:9.5px"><svg width="6" height="6" style="margin-right:5px"><use href="#i-mail"/></svg>rbrentconstruction@mailbox-example.net</li>
    <li style="height:9.5px"><svg width="6" height="6" style="margin-right:5px"><use href="#i-web"/></svg>rbrentconstruction. example.net</li>
  </ul>
</section>

<!-- Card 2 -->
<section class="sign sign--card" style="left:425px">
  <p class="tagline" style="left:19px;top:9px;font-size:9.5px;color:var(--ink-soft)">Residential Construction<br>and Carpentry</p>
  <div class="wordmark" style="left:0;right:0;top:66px;text-align:center;font-size:11px"><span>R Brent</span><span>Construction</span></div>
  <ul class="contacts" style="left:19px;right:12px;top:144px;font-size:6.3px;display:flex;justify-content:space-between">
    <li><svg width="6" height="6" style="margin-right:5px"><use href="#i-phone"/></svg>0493 518 264</li>
    <li><svg width="6" height="6" style="margin-right:5px"><use href="#i-mail"/></svg>rbrentconstruction@mailbox-example.net</li>
    <li><svg width="6" height="6" style="margin-right:5px"><use href="#i-web"/></svg>rbrentconstruction.example.net</li>
  </ul>
</section>

<!-- Card 3 -->
<section class="sign sign--card" style="left:779px">
  <div class="wordmark" style="left:174px;width:128px;top:52px;text-align:center;font-size:10px"><span>R Brent</span><span>Construction</span></div>
  <div class="rule" style="left:174px;width:128px;top:97px"></div>
  <ul class="contacts" style="left:174px;top:105px;font-size:6.3px">
    <li style="height:9.5px"><svg width="6" height="6" style="margin-right:5px"><use href="#i-phone"/></svg>0493 518 264</li>
    <li style="height:9.5px"><svg width="6" height="6" style="margin-right:5px"><use href="#i-mail"/></svg>rbrentconstruction@mailbox-example.net</li>
    <li style="height:9.5px"><svg width="6" height="6" style="margin-right:5px"><use href="#i-web"/></svg>rbrentconstruction. example.net</li>
  </ul>
  <div class="rule" style="left:174px;width:128px;top:139px"></div>
  <p class="tagline" style="left:18px;top:139px;font-size:6px">Residential Construction<br>and Carpentry</p>
</section>

</body>
</html>
```